Thanksgiving Postcard with my family photo on front from my dental office

I just want to send out a Thaksgiving postcard of my family to patients at my dental practice: I want the entire front to be a photo of the family that I have downloaded. I want to get it done soon since Thanksgiving is here. 5x7 preferable

Industry/Entity Type

Dental

```html
<!DOCTYPE html>
<html lang="en">
<head>
<meta charset="utf-8">
<title>Bright Arc Dental Holiday Postcard</title>
<link rel="stylesheet" href="https://fonts.googleapis.com/css2?family=Schoolbell&display=swap">
<style>
  :root {
    --brand-red: #d8232a;
    --brand-orange: #f39a1e;
    --blush: #f5bcc3;
    --ink: #333333;
    --paper: #ffffff;
    --photo-dark: #3a3a2c;
    --photo-mid: #8a6a3c;
    --photo-warm: #c6552a;
  }
  * { margin: 0; padding: 0; box-sizing: border-box; }
  html, body { width: 833px; height: 1200px; overflow: hidden; background: var(--paper); }
  .postcard { position: relative; width: 833px; height: 1200px; background: var(--paper); overflow: hidden; }
  .family-photo {
    position: absolute; left: 0; top: 0; width: 833px; height: 598px;
    background: linear-gradient(180deg, var(--photo-dark) 0%, #5c5a3a 35%, var(--photo-mid) 60%, var(--photo-warm) 78%, #2b2622 100%);
  }
  .photo-brand {
    position: absolute; left: 58px; top: 26px; display: flex; align-items: center; gap: 10px;
    font-family: Arial, Helvetica, sans-serif; font-weight: 700; font-size: 22px; line-height: 1.05;
    color: var(--paper);
  }
  .photo-brand .dot { width: 34px; height: 34px; border-radius: 50%; background: var(--paper); }
  .accent-top { position: absolute; left: 686px; top: 607px; width: 147px; height: 145px; background: var(--blush); }
  .accent-right { position: absolute; left: 506px; top: 843px; width: 327px; height: 357px; background: var(--blush); }
  .accent-bottom { position: absolute; left: 268px; top: 1124px; width: 565px; height: 76px; background: var(--blush); }
  .band-brand {
    position: absolute; left: 40px; top: 628px; display: flex; align-items: center; gap: 12px;
    font-family: Arial, Helvetica, sans-serif; font-weight: 700; font-size: 28px; line-height: 1.05;
    color: var(--brand-red);
  }
  .band-brand .dot { width: 54px; height: 54px; border-radius: 50%; background: var(--brand-orange); }
  .address {
    position: absolute; left: 469px; top: 634px;
    font-family: Arial, Helvetica, sans-serif; font-weight: 700; font-size: 18px; line-height: 21px;
    color: var(--brand-red); font-style: normal;
  }
  .message {
    position: absolute; left: 82px; top: 740px; width: 430px;
    font-family: "Schoolbell", cursive; font-size: 22px; line-height: 30.5px; color: var(--ink);
  }
  .message p + p { margin-top: 30px; }
  .sign-off {
    position: absolute; left: 86px; top: 1068px; width: 400px;
    font-family: "Schoolbell", cursive; font-size: 22px; line-height: 30.5px; color: var(--ink);
  }
</style>
</head>
<body>
<main class="postcard">
  <section class="family-photo" role="img" aria-label="Family portrait of five seated on autumn leaves in a park, trees behind">
    <div class="photo-brand"><span class="dot"></span><span>BRIGHT ARC<br>DENTAL, INC</span></div>
  </section>

  <div class="accent-top"></div>
  <div class="accent-right"></div>
  <div class="accent-bottom"></div>

  <div class="band-brand"><span class="dot"></span><span>BRIGHT ARC<br>DENTAL, INC</span></div>

  <address class="address">
    Bright Arc Dental, Inc.<br>
    1427 Harbor View Rd<br>
    Fairhope, AL 36532
  </address>

  <div class="message">
    <p>As the holiday season is upon us, there is no time more fitting to think about all that we are grateful for and say thank you to those who have made our progress possible.</p>
    <p>We truly appreciate your business and hope that the holidays and the coming year will bring you happiness and success.</p>
  </div>

  <p class="sign-off">Best wishes from your Bright Arc<br>Family</p>
</main>
</body>
</html>
```